Motivational Vision Board for my future life

My name is Brent Holloway I want to create a 2 feet wide by 3 feet tall vertical vision board design for motivation and goal setting. Motivational quotes and pictures and anything else you can think of. I want to make 1 million dollars a year, work two hours a day. Have a house on the beach on the water with my bedroom overlooking the water. Wife and kids with a dog. Strong faith with god being the center of everything as I am a Christian. 185 lbs shredded with muscle. Traveling the world and being happy.

Requirements
Must have
• Pictures, quotes, my goals and everything I mentioned.

```html
<!DOCTYPE html>
<html lang="en">
<head>
<meta charset="UTF-8">
<title>Motivational Vision Board for My Future Life</title>
<link rel="stylesheet" href="https://fonts.googleapis.com/css2?family=Oswald:wght@400;500;600&display=swap">
<style>
  :root {
    --cork: #b98a58;
    --cork-dark: #a87a4b;
    --frame: #ffffff;
    --ink: #1d1d1d;
    --teal: #3f8f94;
    --blue: #2f6fb7;
    --peach: #fde4c8;
    --sky: #eef4fb;
    --white: #ffffff;
  }
  * { margin: 0; padding: 0; box-sizing: border-box; }
  html, body { width: 802px; height: 1200px; overflow: hidden; background: var(--frame); }
  .board {
    position: relative;
    width: 802px; height: 1200px;
    background: radial-gradient(ellipse at 50% 40%, var(--cork), var(--cork-dark));
    border: 8px solid var(--frame);
    font-family: "Oswald", "Arial Narrow", sans-serif;
    text-transform: uppercase;
  }
  .board-title {
    position: absolute; left: 380px; top: 52px; width: 390px;
    color: var(--white); font-weight: 500;
  }
  .board-title__main { font-size: 25px; letter-spacing: 0.5px; line-height: 1.1; }
  .board-title__sub {
    display: flex; align-items: center; gap: 8px;
    font-size: 23px; line-height: 1.3; margin-top: 8px;
  }
  .board-title__sub::before {
    content: ""; width: 96px; height: 3px; background: var(--white);
  }
  .goal-card {
    position: absolute; display: flex; align-items: stretch;
    box-shadow: 2px 3px 6px rgba(0,0,0,0.25);
    padding: 6px;
  }
  .goal-card__photo { flex: none; height: 100%; }
  .goal-card__text {
    flex: 1; display: flex; align-items: center;
    padding: 0 10px; font-weight: 500; line-height: 1.15;
  }
  .goal-faith { left: 40px; top: 51px; width: 326px; height: 214px; background: var(--white); }
  .goal-faith .goal-card__photo { width: 192px; background: linear-gradient(160deg, #f5e3b0 0%, #8fae7b 45%, #3f5a3a 100%); }
  .goal-faith .goal-card__text { font-size: 15px; font-weight: 400; color: var(--ink); align-items: flex-start; padding-top: 4px; }

  .goal-home { left: 393px; top: 179px; width: 353px; height: 235px; background: var(--peach); }
  .goal-home .goal-card__photo { width: 227px; background: linear-gradient(180deg, #cfe8f2 0%, #7cc8d9 45%, #efd7a9 80%, #e5c58c 100%); }
  .goal-home .goal-card__text { font-size: 19px; color: var(--teal); }

  .goal-wealth { left: 45px; top: 433px; width: 348px; height: 235px; background: var(--sky); }
  .goal-wealth .goal-card__photo { width: 208px; background: linear-gradient(135deg, #f7f3e6 0%, #dfe9ef 50%, #5b7186 100%); }
  .goal-wealth .goal-card__text { font-size: 21px; color: var(--teal); }

  .goal-family { left: 414px; top: 567px; width: 331px; height: 254px; background: var(--white); }
  .goal-family .goal-card__photo { width: 205px; background: linear-gradient(160deg, #f3efd9 0%, #d9b89a 50%, #6f8f52 100%); }
  .goal-family .goal-card__text { font-size: 30px; color: var(--ink); }

  .goal-fitness { left: 40px; top: 762px; width: 348px; height: 192px; background: var(--white); }
  .goal-fitness .goal-card__photo { width: 160px; background: linear-gradient(180deg, #a9c9e6 0%, #c88a5e 45%, #8a5535 100%); }
  .goal-fitness .goal-card__text { font-size: 36px; color: var(--blue); }

  .goal-travel { left: 406px; top: 895px; width: 340px; height: 192px; background: var(--peach); }
  .goal-travel .goal-card__photo { width: 173px; background: linear-gradient(180deg, #f6d48b 0%, #b7cfd6 40%, #4f7a5a 100%); }
  .goal-travel .goal-card__text { font-size: 26px; color: var(--ink); }
</style>
</head>
<body>
<main class="board">
  <header class="board-title">
    <div class="board-title__main">Motivational Vision Board</div>
    <div class="board-title__sub">For My Future Life</div>
  </header>

  <section class="goal-card goal-faith">
    <div class="goal-card__photo" role="img" aria-label="A couple embracing in a garden before a glowing cross"></div>
    <p class="goal-card__text">Strong faith with God being the center of everything as I am a Christian.</p>
  </section>

  <section class="goal-card goal-home">
    <div class="goal-card__photo" role="img" aria-label="Modern beach house on the shore overlooking the ocean with palm trees"></div>
    <p class="goal-card__text">Have a house on the beach on the water with my bedroom overlooking the water.</p>
  </section>

  <section class="goal-card goal-wealth">
    <div class="goal-card__photo" role="img" aria-label="Illustration of a relaxed man at a laptop with the headline make 1 million dollars a year working only two hours a day"></div>
    <p class="goal-card__text">I want to make 1 million dollars a year, work two hours a day.</p>
  </section>

  <section class="goal-card goal-family">
    <div class="goal-card__photo" role="img" aria-label="Mother with two children and a dog outdoors"></div>
    <p class="goal-card__text">Wife and kids with a dog.</p>
  </section>

  <section class="goal-card goal-fitness">
    <div class="goal-card__photo" role="img" aria-label="Muscular shredded man standing outdoors"></div>
    <p class="goal-card__text">185 lbs shredded with muscle.</p>
  </section>

  <section class="goal-card goal-travel">
    <div class="goal-card__photo" role="img" aria-label="Traveler with arms raised on a mountain top at sunrise"></div>
    <p class="goal-card__text">Traveling the world and being happy.</p>
  </section>
</main>
</body>
</html>
```